Commercial brochure presenting independent commercial activity

I would like to create a commercial brochure for my new professional activity.

This is a personal and not business oriented brochure because I will become an independent project assistant to assist engineering offices with one-off missions.

I want a 4 page A4 brochure

• Page 1: Logo, personal photo
• Page 2 and 3: Personal presentation and presentation of my activities
• Page4: contact information

My target audience: engineering offices and design offices

The objective of the brochure: it is to make my profile interesting so that design offices will want to use my services when there is demand

Sector of activity: food, chemical, pharmaceutical industry
The text of the brochure must remain in French and contain what is in the attached file

On page 1, you must keep a space for a photo of my profile which I will insert later because I do not have it yet and insert my monogram (it can be reworked to be inserted in the brochure)
The image with the logo (R/M) is the color range I want

Target Market(s)

engineering offices and design offices

Industry/Entity Type

industrie alimentaire, chimique, pharmaceutique

Font styles to use
Sans Serif

Colors
0094D4
00A9DD
6FCCEA
C7EBF8
E9F6FB

Requirements
Must have
• The plate must comply with current codes. Each reader must think that I am dynamic and that my services are of quality and equivalent to the presentation

```html
<!DOCTYPE html>
<html lang="fr">
<head>
<meta charset="utf-8">
<title>Brochure – Lucien Marvaux-Delorme</title>
<link href="https://fonts.googleapis.com/css2?family=Poppins:wght@400;500;600;700&display=swap" rel="stylesheet">
<style>
:root{
  --blue:#0089c6;
  --blue-light:#00a9dd;
  --ink:#1c1c1c;
  --text:#333;
  --stage:#9b9b9d;
  --card:#d6d6d6;
  --white:#fff;
}
*{margin:0;padding:0;box-sizing:border-box}
html,body{width:800px;height:1200px;overflow:hidden;background:var(--stage)}
body{font-family:"Poppins",sans-serif;color:var(--text)}
.canvas{position:relative;width:800px;height:1200px}
.page{position:absolute;width:343px;height:486px;background:var(--white);overflow:hidden;box-shadow:0 2px 6px rgba(0,0,0,.18)}
.page--cover{left:40px;top:46px}
.page--profile{left:416px;top:46px}
.page--advantages{left:40px;top:584px}
.page--contact{left:416px;top:584px}
.abs{position:absolute}
.photo{position:absolute}

/* brand name */
.brand{position:absolute;text-align:center;color:var(--blue);font-weight:400;white-space:nowrap}
.brand__name{display:block}
.brand__tag{display:block;font-size:5px;margin-top:2px}
.brand__dot{display:inline-block;border-radius:50%;background:var(--blue)}

/* cover */
.cover__accent{right:0;top:0;width:44px;height:116px;background:var(--blue)}
.cover__brand{left:20px;top:60px;width:190px}
.cover__brand .brand__dot{width:18px;height:18px;margin-bottom:6px}
.cover__brand .brand__name{font-size:11.5px}
.cover__photo{left:47px;top:121px;width:296px;height:189px;background:linear-gradient(135deg,#e9eef2 0%,#c9b8a8 40%,#5d6f86 65%,#eef1f4 100%)}
.cover__frame{left:228px;top:255px}
.cover__name{left:46px;top:326px;color:var(--blue);font-weight:700;font-size:27px;line-height:29px}
.cover__tagline{left:47px;top:389px;font-size:12.5px;font-weight:500;color:var(--ink);line-height:15px}
.cover__url{left:47px;top:440px;font-size:10.5px;color:var(--ink);letter-spacing:.3px}
.cover__url b{color:var(--blue);font-weight:600}

/* profile */
.profile__accent{right:0;top:0;width:47px;height:82px;background:var(--blue)}
.profile__title{left:32px;top:34px;color:var(--blue);font-weight:700;font-size:12px;line-height:14.5px;text-transform:uppercase}
.profile__subtitle{left:32px;top:65px;font-size:7.2px;font-weight:600;color:var(--ink)}
.profile__intro{left:32px;top:81px;width:168px;font-size:5.1px;line-height:6.2px;text-align:justify;color:var(--ink)}
.profile__thumb{left:218px;top:33px;width:101px;height:80px;border:2px solid #fff;box-shadow:0 1px 4px rgba(0,0,0,.25);background:linear-gradient(135deg,#2c2a2c 0%,#c79a4a 45%,#eceae6 70%,#8a8a8a 100%)}
.profile__hero{left:32px;top:139px;width:120px;height:255px;border-radius:0 26px 0 26px;border:2px solid #fff;box-shadow:0 1px 4px rgba(0,0,0,.25);background:linear-gradient(180deg,#cfd4d8 0%,#9aa1a6 35%,#5e6368 55%,#d6d6d6 80%,#e6e6e6 100%)}
.services{left:175px;top:143px;width:150px}
.services__group{margin-bottom:7px}
.services__head{font-size:8px;font-weight:600;color:var(--ink);margin-bottom:2px}
.services__list{list-style:none}
.services__list li{position:relative;padding-left:7px;font-size:5.2px;line-height:6.4px;color:var(--ink);margin-bottom:4px}
.services__list--tight li{margin-bottom:3.5px}
.services__list li::before{content:"";position:absolute;left:0;top:1.6px;width:3.6px;height:3.6px;border-radius:50%;background:var(--blue)}

.footer-brand{left:30px;top:437px;text-align:left}
.footer-brand .brand__name{font-size:9px}
.footer-brand .brand__tag{font-size:4.4px;margin-top:0}
.footer-url{right:30px;top:441px;font-size:6.8px;color:var(--ink);display:flex;align-items:center;gap:4px}
.footer-url b{font-weight:600}
.page-badge{display:inline-flex;width:11px;height:11px;border-radius:50%;background:var(--blue);color:#fff;font-size:5px;align-items:center;justify-content:center}

/* advantages */
.adv__band{left:0;top:0;width:343px;height:106px;background:var(--blue)}
.adv__title{left:0;top:18px;width:343px;text-align:center;color:#fff;font-weight:700;font-size:11.5px}
.adv__card{top:54px;width:71px;height:119px;background:var(--card);border-radius:7px;text-align:center;padding:19px 5px 0}
.adv__card h3{font-size:6.2px;line-height:8px;font-weight:700;color:var(--ink);text-transform:uppercase;margin-bottom:9px}
.adv__card p{font-size:5px;line-height:6.2px;color:#444}
.adv__card::after{content:"";position:absolute;left:16px;bottom:0;width:39px;height:3px;border-radius:2px 2px 0 0;background:var(--blue)}
.adv__icon{position:absolute;left:24px;top:-12px}
.unique__title{left:22px;top:188px;font-size:11.5px;font-weight:700;color:var(--ink)}
.unique__title span{color:var(--blue)}
.unique__text{left:22px;top:205px;width:166px;font-size:5.1px;line-height:6.2px;text-align:justify;color:var(--ink)}
.unique__lead{left:22px;top:229px;font-size:5px;color:var(--ink)}
.unique__rate{left:20px;top:234px;font-size:25px;font-weight:700;color:var(--blue);line-height:28px}
.unique__rule{left:85px;top:231px;height:27px;border-left:1px dashed #444}
.unique__note{left:96px;top:235px;width:86px;font-size:5px;line-height:6.2px;color:var(--ink)}
.unique__photo{left:219px;top:192px;width:103px;height:66px;border:2px solid #fff;box-shadow:0 1px 4px rgba(0,0,0,.25);background:linear-gradient(135deg,#3a3a3a 0%,#b79a6c 35%,#e7e4de 65%,#bdbdbd 100%)}
.unique__cta{left:22px;top:269px;width:305px;font-size:7.2px;line-height:8.6px;font-weight:600;color:var(--ink)}
.adv__team{left:0;top:293px;width:343px;height:193px;background:linear-gradient(180deg,#ffffff 0%,#d8d8d8 18%,#8d8d8d 45%,#6e6e6e 65%,#cfcfcf 88%,#ffffff 100%)}

/* contact */
.contact__bg{left:0;top:0;width:343px;height:486px;background:linear-gradient(180deg,#f4f4f4 0%,#ececec 45%,#d5d5d5 75%,#c4c4c4 100%)}
.contact__brand{left:71px;top:226px;width:200px}
.contact__brand .brand__dot{width:16px;height:16px;margin-bottom:6px}
.contact__brand .brand__name{font-size:11px}
.contact__panel{left:83px;top:319px;width:177px;height:167px;background:var(--blue);border-radius:26px 0 0 0;color:#fff;text-align:center}
.contact__item{position:absolute;left:0;width:177px;font-size:8.6px;line-height:10.5px}
.contact__icon{display:block;margin:0 auto 4px;width:14px;height:14px;border-radius:50%;background:var(--ink)}
</style>
</head>
<body>
<main class="canvas">

  <!-- Page 1 : couverture -->
  <section class="page page--cover">
    <div class="abs cover__accent"></div>
    <div class="brand cover__brand">
      <span class="brand__dot"></span>
      <span class="brand__name">Lucien Marvaux-Delorme</span>
      <span class="brand__tag">Assistant de projet indépendant</span>
    </div>
    <div class="photo cover__photo" role="img" aria-label="Photo d'équipe : trois collègues autour d'une tablette dans un bureau d'études"></div>
    <svg class="abs cover__frame" width="83" height="92" viewBox="0 0 83 92" aria-hidden="true">
      <path d="M80 20 V2.5 H2.5 V89.5 H80 V72" fill="none" stroke="var(--blue)" stroke-width="5"/>
    </svg>
    <h1 class="abs cover__name">Lucien<br>Marvaux-Delorme</h1>
    <p class="abs cover__tagline">Un atout précieux pour votre<br>bureau d'études</p>
    <p class="abs cover__url">www.<b>lucienmarvaux-delorme</b>.in</p>
  </section>

  <!-- Page 2 : profil et compétences -->
  <section class="page page--profile">
    <div class="abs profile__accent"></div>
    <h2 class="abs profile__title">Lucien<br>Marvaux-Delorme</h2>
    <p class="abs profile__subtitle">Un atout précieux pour votre bureau d'études</p>
    <p class="abs profile__intro">Avec plus de 30 ans d'expérience dans l'industrie, je suis un expert chevronné en conception, gestion de projets et sécurité. J'offre mes services d'assistant de projet indépendant pour vous aider à gérer les pics de charge et les besoins spécifiques de votre bureau d'études.</p>
    <div class="photo profile__thumb" role="img" aria-label="Maquette de maison posée sur des plans d'architecte"></div>
    <div class="photo profile__hero" role="img" aria-label="Salle de réunion vitrée avec une présentation en cours"></div>

    <div class="abs services">
      <div class="services__group">
        <h3 class="services__head">Conception &amp; Design</h3>
        <ul class="services__list">
          <li>Maquettes 3D (Modeleur Plant 3D)</li>
          <li>Plans, schémas, RI/P&amp;ID, Flowsheets</li>
          <li>Spécifications, catalogues, définition des fournitures</li>
        </ul>
      </div>
      <div class="services__group">
        <h3 class="services__head">Conception &amp; Design</h3>
        <ul class="services__list services__list--tight">
          <li>Rédaction d'appels d'offre</li>
          <li>Préparation de budgets</li>
          <li>Réalisation de plannings</li>
          <li>Estimations budgétaires</li>
        </ul>
      </div>
      <div class="services__group">
        <h3 class="services__head">Sécurité</h3>
        <ul class="services__list services__list--tight">
          <li>Sécurité machine</li>
          <li>Plans de montage</li>
          <li>Edition de PHS</li>
        </ul>
      </div>
      <div class="services__group">
        <h3 class="services__head">Documentation Technique</h3>
        <ul class="services__list services__list--tight">
          <li>DESP</li>
          <li>Documentations spécifiques</li>
        </ul>
      </div>
      <div class="services__group">
        <h3 class="services__head">Expertise</h3>
        <ul class="services__list">
          <li>Ma connaissance approfondie de la métallurgie (tuyauterie, serrurerie, chaudronnerie, charpente métallique, montage) me permet de garantir des études complètes et d'évite les oublis.</li>
        </ul>
      </div>
    </div>

    <div class="brand footer-brand">
      <span class="brand__name">Lucien Marvaux-Delorme</span>
      <span class="brand__tag">Assistant de projet indépendant</span>
    </div>
    <p class="abs footer-url">www.<b>lucienmarvaux-delorme</b>.in <span class="page-badge">01</span></p>
  </section>

  <!-- Page 3 : avantages -->
  <section class="page page--advantages">
    <div class="abs adv__band"></div>
    <h2 class="abs adv__title">VOTRE AVANTAGE</h2>

    <article class="abs adv__card" style="left:22px">
      <svg class="adv__icon" width="23" height="23" viewBox="0 0 23 23" aria-hidden="true"><circle cx="11.5" cy="11.5" r="11" fill="none" stroke="var(--blue)" stroke-dasharray="2 1.5"/><circle cx="11.5" cy="11.5" r="9" fill="#2b2b2b"/><circle cx="11.5" cy="11.5" r="3.5" fill="none" stroke="#fff" stroke-width="1.2"/></svg>
      <h3>Connaissance des besoins des concepteurs et des fabricants</h3>
      <p>J'ai travaillé des deux côtés, ce qui me permet de comprendre les défis et les attentes de chacun.</p>
    </article>
    <article class="abs adv__card" style="left:98.5px">
      <svg class="adv__icon" width="23" height="23" viewBox="0 0 23 23" aria-hidden="true"><circle cx="11.5" cy="11.5" r="11" fill="none" stroke="var(--blue)" stroke-dasharray="2 1.5"/><circle cx="11.5" cy="11.5" r="9" fill="#2b2b2b"/><path d="M11.5 16V7M8.5 10l3-3 3 3" fill="none" stroke="#fff" stroke-width="1.2"/></svg>
      <h3>Flexibilité</h3>
      <p>Je suis disponible pour des missions ponctuelles et à durée déterminée, sans engagement à long terme.</p>
    </article>
    <article class="abs adv__card" style="left:175px">
      <svg class="adv__icon" width="23" height="23" viewBox="0 0 23 23" aria-hidden="true"><circle cx="11.5" cy="11.5" r="11" fill="none" stroke="var(--blue)" stroke-dasharray="2 1.5"/><circle cx="11.5" cy="11.5" r="9" fill="#2b2b2b"/><circle cx="11.5" cy="11.5" r="4.5" fill="none" stroke="#fff" stroke-width="1.2" stroke-dasharray="2 1"/></svg>
      <h3>Efficacité</h3>
      <p>Je peux vous aider à gérer les surcharges de travail et à respecter vos délais.</p>
    </article>
    <article class="abs adv__card" style="left:251.5px">
      <svg class="adv__icon" width="23" height="23" viewBox="0 0 23 23" aria-hidden="true"><circle cx="11.5" cy="11.5" r="11" fill="none" stroke="var(--blue)" stroke-dasharray="2 1.5"/><circle cx="11.5" cy="11.5" r="9" fill="#2b2b2b"/><path d="M7.5 11.5l3 3 5-6" fill="none" stroke="#fff" stroke-width="1.3"/></svg>
      <h3>Collaboration fluide</h3>
      <p>Je suis à votre disposition pour discuter de vos besoins et vous proposer des solutions sur mesure.</p>
    </article>

    <h2 class="abs unique__title">UN ATOUT <span>UNIQUE</span></h2>
    <p class="abs unique__text">Malgré mon handicap en fauteuil roulant, je suis totalement opérationnel et mon expérience me permet de vous offrir une expertise de haut niveau.</p>
    <p class="abs unique__lead">Je suis disponible à</p>
    <p class="abs unique__rate">35%</p>
    <div class="abs unique__rule"></div>
    <p class="abs unique__note">dès septembre 2024 et je suis prêt à mettre mon expertise et mon dynamisme au service de votre succès.</p>
    <div class="photo unique__photo" role="img" aria-label="Mains travaillant sur des plans techniques"></div>
    <p class="abs unique__cta">N'hésitez pas à me contacter pour discuter de vos besoins et découvrir comment je peux vous aider à atteindre vos objectifs.</p>
    <div class="photo adv__team" role="img" aria-label="Équipe en réunion autour d'une grande table, en noir et blanc"></div>

    <div class="brand footer-brand" style="left:22px;top:446px">
      <span class="brand__name">Lucien Marvaux-Delorme</span>
      <span class="brand__tag">Assistant de projet indépendant</span>
    </div>
    <p class="abs footer-url" style="right:24px;top:450px">www.<b>lucienmarvaux-delorme</b>.in <span class="page-badge">02</span></p>
  </section>

  <!-- Page 4 : contact -->
  <section class="page page--contact">
    <div class="photo contact__bg" role="img" aria-label="Immeubles de bureaux en fond clair estompé"></div>
    <div class="brand contact__brand">
      <span class="brand__dot"></span>
      <span class="brand__name">Lucien Marvaux-Delorme</span>
      <span class="brand__tag">Assistant de projet indépendant</span>
    </div>
    <address class="abs contact__panel" style="font-style:normal">
      <div class="contact__item" style="top:19px">
        <svg class="contact__icon" viewBox="0 0 14 14" aria-hidden="true"><circle cx="7" cy="7" r="7" fill="#1c1c1c"/><path d="M5 4.2l1.2 1.6-.7.8c.5 1 1.1 1.6 2 2l.8-.7 1.6 1.2-.6 1c-2.5-.3-4.6-2.4-4.9-4.9z" fill="#fff"/></svg>
        +41 79 512 38 04
      </div>
      <div class="contact__item" style="top:57px">
        <svg class="contact__icon" viewBox="0 0 14 14" aria-hidden="true"><circle cx="7" cy="7" r="7" fill="#1c1c1c"/><path d="M7 3.2a2.6 2.6 0 0 1 2.6 2.6C9.6 7.8 7 10.8 7 10.8S4.4 7.8 4.4 5.8A2.6 2.6 0 0 1 7 3.2z" fill="#fff"/><circle cx="7" cy="5.8" r="1" fill="#1c1c1c"/></svg>
        Ch. des Tilleuls 8<br>1872 Valdorge
      </div>
      <div class="contact__item" style="top:106px">
        <svg class="contact__icon" viewBox="0 0 14 14" aria-hidden="true"><circle cx="7" cy="7" r="7" fill="#1c1c1c"/><rect x="3.8" y="4.8" width="6.4" height="4.6" fill="#fff"/><path d="M3.8 4.8L7 7.4l3.2-2.6" fill="none" stroke="#1c1c1c" stroke-width=".7"/></svg>
        lucien@marvaux-delorme.ch
      </div>
    </address>
  </section>

</main>
</body>
</html>
```